SIGN UP PAGE AND CHECK OUT PROCESS DESIGN NEEDED

I offer a subscription service. Two products that offer the same exact features just two different prices as the cheaper product offers limited of all the features....<br/><br/>PLEASE USE EXISTING THEME OF CURRENT DESIGN JUST MAKE AN IMPROVED SIGN UP PAGE. <br/><br/><br/>NEED SIGN UP PAGE for a subscription service..... <br/>This is my current sign up page, only offers one product: https://www.brightloomrewards.biz/?page=signup <br/><br/>Please use all the same fields and content listed on this sign up page also please do a fake sign up to see the credit card page. I also need the credit card page to be designed....or if you want to combine the sign up and credit card page, etc. all in one I am open for that too....my goal is a super quick an easy sign up for customer. <br/><br/> AL A CARTE PROGRAM<br/>1 CERTIFICATE TYPE EACH MONTH<br/>$49/MTH MONTH TO MONTH BASIS NO CONTRACTS<br/>$239 ONE TIME PAYMENT FOR 6 MTHS OF SERVICE<br/>$399 ONE TIME PAYMENT FOR 12 MONTHS OF SERVICE<br/><br/>FEATURES:<br/><br/>UNLIMITED CERTIFICATE PDF DOWNLOADS<br/><br/>UNLIMITED E-MAIL CERTIFICATES<br/><br/>UNLIMITED TEXT/SMS CERTIFICATES<br/><br/>UNLIMITED API USAGE<br/><br/>UNLIMITED WEB BANNER CERTIFICATES<br/><br/>FULL REDEMPTION TRACKING<br/><br/>CERTIFICATE DISTRIBUTION REPORTS<br/><br/>WHITE LABEL REDEMPTION SITE<br/><br/>END USER MARKETING VIDEOS<br/><br/>MARKETING POSTERS AND FLYERS<br/><br/>PRODUCT DESCRIPTIONI BROCHURES<br/><br/>THE LATEST TIPS<br/><br/>SEPERATE REDEMPTION WEBSITES<br/><br/>CONTACT US 24/7<br/><br/>AFFILIATE PROGRAM<br/><br/>DISCOUNT TRAVEL BOOKING ENGINE<br/><br/>UNLIMITED PROGRAM<br/>UNLIMITED AMOUNTS OF ALL THE CERTIFICATES<br/>$99/MTH MONTH TO MONTH BASIS NO CONTRACTS<br/>$495 ONE TIME PAYMENT FOR 6 MTHS OF SERVICE<br/>$2,295 ONE TIME PAYMENT FOR 12 MONTHS OF SERVICE<br/><br/>FEATURES:<br/><br/>UNLIMITED CERTIFICATE PDF DOWNLOADS<br/><br/>UNLIMITED E-MAIL CERTIFICATES<br/><br/>UNLIMITED TEXT/SMS CERTIFICATES<br/><br/>UNLIMITED API USAGE<br/><br/>UNLIMITED WEB BANNER CERTIFICATES<br/><br/>FULL REDEMPTION TRACKING<br/><br/>CERTIFICATE DISTRIBUTION REPORTS<br/><br/>WHITE LABEL REDEMPTION SITE<br/><br/>END USER MARKETING VIDEOS<br/><br/>MARKETING POSTERS AND FLYERS<br/><br/>PRODUCT DESCRIPTIONI BROCHURES<br/><br/>THE LATEST TIPS<br/><br/>SEPERATE REDEMPTION WEBSITES<br/><br/>CONTACT US 24/7<br/><br/>AFFILIATE PROGRAM<br/><br/>DISCOUNT TRAVEL BOOKING ENGINE<br/><br/><br/>

Target Market(s)

B2B SMALL BUSINESS OWNERS
MARKETERS
ADVERTISERS

Industry/Entity Type

Digital Marketing

Number of Pages Required

3 page

Colors

Designer to choose colors to be used in the design.

Requirements
Must have
• MUST MATCH EXISTING THEME
Nice to have
• A VERY MODERN DESIGN

```html
<!DOCTYPE html>
<html lang="en">
<head>
<meta charset="utf-8">
<title>Brightloom Rewards – Sign Up</title>
<link href="https://fonts.googleapis.com/css2?family=Barlow:wght@400;500;600&display=swap" rel="stylesheet">
<style>
:root{
  --bg:#e6fbfb;
  --ink:#1f1f1f;
  --muted:#555b63;
  --blue:#125fba;
  --blue-dark:#0f4f9c;
  --black:#141414;
  --tab:#2b2b2b;
  --line:#c9ced6;
  --card:#ffffff;
  --red:#d33;
  --white:#ffffff;
}
*{box-sizing:border-box;margin:0;padding:0}
html,body{width:672px;height:1200px;overflow:hidden;background:var(--bg)}
body{font-family:"Barlow",Arial,sans-serif;color:var(--ink)}
.stage{position:absolute;left:0;top:0;width:1443px;height:2576px;transform:scale(.46569);transform-origin:0 0}
.page{position:absolute;width:673px;background:linear-gradient(160deg,#fbfbfd 0%,#f1f3f8 45%,#f7f2f4 70%,#eef2f8 100%);box-shadow:0 0 6px rgba(0,0,0,.15)}
.page-signup{left:40px;top:75px;height:1333px}
.page-checkout{left:735px;top:74px;height:2431px}

/* header */
.topbar{position:absolute;left:0;top:0;width:673px;height:70px;background:var(--black)}
.account-tabs{position:absolute;left:470px;top:0;height:17px;display:flex;font-size:8px;color:var(--white)}
.account-tabs span{padding:3px 14px;background:var(--tab)}
.account-tabs .tab-signup{background:var(--blue)}
.brand{position:absolute;left:62px;top:24px;display:flex;align-items:center;gap:6px}
.brand-mark{width:16px;height:16px;background:var(--blue)}
.brand-name{font-size:17px;font-weight:600;color:var(--blue);letter-spacing:1px}
.phone-icon{position:absolute;left:434px;top:34px}
.phone-lines{position:absolute;left:475px;top:31px;font-size:10px;line-height:14px;color:var(--white)}
.phone-lines b{font-weight:600}
.mainnav{position:absolute;left:0;top:70px;width:673px;height:23px;background:var(--blue);display:flex;justify-content:space-between;align-items:center;padding:0 105px 0 86px;font-size:7.5px;color:var(--white)}

/* common text */
.page-title{position:absolute;left:0;width:673px;text-align:center;color:var(--blue);font-weight:500}
.lead{position:absolute;text-align:center;color:var(--ink)}
.card{position:absolute;background:var(--card);box-shadow:0 0 8px rgba(0,0,0,.06);opacity:.96}

/* sign up form */
.signup-form{position:absolute;left:63px;top:275px;width:547px;height:678px}
.form-rows{position:absolute;left:35px;top:28px;width:480px}
.form-row{height:34px;display:flex;align-items:center}
.form-row label{width:122px;font-size:10px;color:var(--ink)}
.form-row label em{color:var(--red);font-style:normal}
.field{width:333px;height:24px;border:1px solid var(--line);background:var(--white);font-size:7px;color:var(--muted);display:flex;align-items:center;justify-content:space-between;padding:0 10px}
.caret{width:0;height:0;border-left:3px solid transparent;border-right:3px solid transparent;border-top:4px solid #333}
.btn{position:absolute;background:var(--blue);color:var(--white);font-size:10px;display:flex;align-items:center;justify-content:center;letter-spacing:.3px}

/* footer */
.footer{position:absolute;left:0;width:673px;height:300px;background:var(--black);color:var(--white)}
.footer h4{position:absolute;top:25px;font-size:10px;font-weight:400}
.quick-links{position:absolute;left:63px;top:43px;list-style:none;font-size:7px;line-height:15.4px;color:#d8d8d8}
.quick-links li::before{content:"› ";}
.contact-block{position:absolute;left:250px;top:41px;font-size:6.5px;line-height:10px;color:#d8d8d8}
.contact-block b{color:var(--white);font-weight:600}
.contact-block .pin,.contact-block .cal{position:absolute;left:0}
.foot-divider{position:absolute;top:20px;width:1px;height:110px;background:#2a2a2a}
.foot-brand{position:absolute;left:485px;top:26px;display:flex;align-items:center;gap:3px}
.foot-brand .brand-mark{width:8px;height:8px}
.foot-brand .brand-name{font-size:8px;letter-spacing:.5px}
.socials{position:absolute;left:509px;top:49px;display:flex;gap:7px}
.socials i{width:14px;height:14px;border-radius:50%;background:var(--blue)}
.socials i.red{background:#e02b20}
.copyright{position:absolute;left:0;width:673px;height:42px;background:var(--blue);color:var(--white);font-size:7.5px;text-align:center;padding-top:16px}
.copyright small{position:absolute;right:40px;top:28px;font-size:7px}

/* checkout */
.verify-card{position:absolute;left:63px;top:217px;width:547px;height:592px}
.avatar{position:absolute;left:35px;top:27px;width:80px;height:80px;border-radius:50%;background:#7b7b7b}
.customer{position:absolute;left:147px;top:28px;font-size:7.5px;line-height:16.4px;color:var(--ink)}
.fees{position:absolute;left:147px;top:158px;font-size:7.5px;line-height:16.4px;color:var(--blue)}
.fees span{display:inline-block;width:90px}
.card-divider{position:absolute;left:0;top:227px;width:547px;height:1px;background:#e3e6eb}
.pay-rows{position:absolute;left:35px;top:245px}
.pay-row{height:36.7px;display:flex;align-items:center;font-size:9.5px}
.pay-row label{width:107px}
.pay-row .colon{width:15px}
.cvv-note{position:absolute;left:159px;top:433px;width:330px;font-size:7px;line-height:16.4px;color:var(--muted)}
.agree{position:absolute;left:159px;top:492px;font-size:7px;color:var(--ink);display:flex;align-items:center;gap:7px}
.agree i{width:8px;height:8px;border:1px solid #bbb;border-radius:50%}

.plan{position:absolute;top:838px;width:263px;height:510px;background:var(--card);border:1px solid #dde2ea}
.plan-head{height:31px;background:var(--blue);color:var(--white);font-size:10px;display:flex;align-items:center;justify-content:center}
.plan-prices{height:106px;border-bottom:1px solid #e3e6eb;text-align:center;font-size:7.5px;line-height:19.2px;padding-top:17px}
.plan-prices b{color:var(--blue);font-weight:500}
.plan h5{font-size:9px;font-weight:500;margin:13px 0 0 13px}
.features{list-style:none;margin:14px 0 0 13px;font-size:7px;line-height:20.2px;color:var(--muted)}
.features li{display:flex;align-items:center;gap:18px}

.terms{position:absolute;left:63px;top:1376px;width:547px;height:660px}
.terms h3{position:absolute;left:35px;top:23px;font-size:13px;font-weight:500}
.term-icon{position:absolute;left:35px;width:51px;height:51px;border-radius:50%;background:var(--blue)}
.term-title{position:absolute;left:107px;font-size:12px;color:var(--blue);font-weight:500}
.term-text{position:absolute;left:107px;width:408px;font-size:7px;line-height:15.4px;color:var(--muted);text-align:justify}
.term-text p+p{margin-top:15.4px}
</style>
</head>
<body>
<div class="stage">

<!-- SIGN UP PAGE -->
<section class="page page-signup">
  <header class="topbar">
    <div class="account-tabs"><span>➜ LOGIN</span><span class="tab-signup">SIGN UP</span></div>
    <div class="brand"><span class="brand-mark"></span><span class="brand-name">BRIGHTLOOM REWARDS</span></div>
    <svg class="phone-icon" width="22" height="22" viewBox="0 0 22 22"><circle cx="11" cy="11" r="11" fill="#125fba"/><path d="M8 6.5l2 2-1 1.3c.6 1.3 1.6 2.3 2.9 2.9l1.3-1 2 2-1.2 1.4c-3.3-.3-6.9-3.9-7.2-7.2z" fill="#fff"/></svg>
    <div class="phone-lines">USA Office : <b>555-014-2290</b><br>International : <b>1-800-555-0148</b></div>
  </header>
  <nav class="mainnav"><span>HOME</span><span>OUR INCENTIVES</span><span>SAMPLES</span><span>AFFILIATES</span><span>TESTIMONIALS</span><span>FAQ</span><span>CONTACT</span></nav>

  <h1 class="page-title" style="top:113px;font-size:17px">SIGN UP</h1>
  <p class="lead" style="left:118px;top:144px;width:440px;font-size:7.5px;line-height:17px">Today you will be charged $99.00 plus a one-time set up fee of $99.00 for a grand total of $198.00 for your first month. You will also be set up on an automatic 30 day recurring billing cycle to be charged $99 every month until you submit a support ticket to cancel. You must submit a support ticket from your back end account at least 3 business days before your next billing date in order not be charged for the following month.</p>
  <p class="lead" style="left:0;top:225px;width:673px;font-size:7.5px;font-weight:500">The information you provide below must match the billing details of where your billing statement is mailed to from your bank.</p>

  <form class="card signup-form">
    <div class="form-rows">
      <div class="form-row"><label>First Name<em>*</em></label><div class="field"></div></div>
      <div class="form-row"><label>Last Name<em>*</em></label><div class="field"></div></div>
      <div class="form-row"><label>Company</label><div class="field"></div></div>
      <div class="form-row"><label>Email Address<em>*</em></label><div class="field"></div></div>
      <div class="form-row"><label>Billing Address<em>*</em></label><div class="field"></div></div>
      <div class="form-row"><label>Billing Address 2<em>*</em></label><div class="field"></div></div>
      <div class="form-row"><label>City<em>*</em></label><div class="field"></div></div>
      <div class="form-row"><label>State<em>*</em></label><div class="field">Select Your State<i class="caret"></i></div></div>
      <div class="form-row"><label>Country<em>*</em></label><div class="field">United States<i class="caret"></i></div></div>
      <div class="form-row"><label>Zip<em>*</em></label><div class="field"></div></div>
      <div class="form-row"><label>Phone<em>*</em></label><div class="field"></div></div>
      <div class="form-row"><label>Username<em>*</em></label><div class="field"></div></div>
      <div class="form-row"><label>Password<em>*</em></label><div class="field"></div></div>
      <div class="form-row"><label>Confirm Password<em>*</em></label><div class="field"></div></div>
      <div class="form-row"><label>Industry<em>*</em></label><div class="field"></div></div>
      <div class="form-row"><label style="font-size:9px">How Did You Hear About Us?<em>*</em></label><div class="field"></div></div>
      <div class="form-row"><label>Promo Code</label><div class="field"></div></div>
    </div>
    <div class="btn" style="left:157px;top:615px;width:336px;height:29px">SIGNUP NOW</div>
  </form>

  <footer class="footer" style="top:991px">
    <h4 style="left:63px">QUICK LINKS</h4>
    <ul class="quick-links"><li>Home</li><li>Our Incentives</li><li>Samples</li><li>Affiliate</li><li>Testimonials</li><li>Faq</li><li>Contact Us</li><li>Terms &amp; Conditions</li><li>Privacy Policy</li><li>Hoteliers</li><li>BLR PDF Flyer</li><li>BLR PDF Brochure</li><li>BLR Certificates List</li><li>How To Use BLR Certificates</li><li>Free Video Ad Mock Up For Marketing</li></ul>
    <div class="foot-divider" style="left:243px"></div>
    <h4 style="left:250px">CONTACT DETAILS</h4>
    <div class="contact-block">
      <svg class="pin" width="7" height="9" viewBox="0 0 7 9"><path d="M3.5 0A3.5 3.5 0 0 0 0 3.5C0 6 3.5 9 3.5 9S7 6 7 3.5A3.5 3.5 0 0 0 3.5 0z" fill="#ccc"/><circle cx="3.5" cy="3.5" r="1.3" fill="#141414"/></svg>
      <div style="padding-left:12px"><b>Brightloom Rewards Group, Inc.</b><br>410 Harbor View Lane<br>Oakridge CA 90210</div>
      <svg class="cal" style="top:53px" width="9" height="8" viewBox="0 0 9 8"><rect x="0" y="1" width="9" height="7" fill="#ccc"/><rect x="1" y="3" width="7" height="4" fill="#141414"/></svg>
      <div style="padding-left:12px;margin-top:22px">Hours: Mon-Fri 8am - 5pm PST<br>Sat-Sun CLOSED</div>
    </div>
    <div class="foot-divider" style="left:477px"></div>
    <div class="foot-brand"><span class="brand-mark"></span><span class="brand-name">BRIGHTLOOM REWARDS</span></div>
    <div class="socials"><i></i><i class="red"></i><i></i><i></i></div>
  </footer>
  <div class="copyright" style="top:1291px">Copyright 2005-2020 Brightloom Rewards Group,Inc. All Rights Reserved<small>C2</small></div>
</section>

<!-- CHECKOUT PAGE -->
<section class="page page-checkout">
  <header class="topbar">
    <div class="account-tabs"><span>➜ LOGIN</span><span class="tab-signup">SIGN UP</span></div>
    <div class="brand"><span class="brand-mark"></span><span class="brand-name">BRIGHTLOOM REWARDS</span></div>
    <svg class="phone-icon" width="22" height="22" viewBox="0 0 22 22"><circle cx="11" cy="11" r="11" fill="#125fba"/><path d="M8 6.5l2 2-1 1.3c.6 1.3 1.6 2.3 2.9 2.9l1.3-1 2 2-1.2 1.4c-3.3-.3-6.9-3.9-7.2-7.2z" fill="#fff"/></svg>
    <div class="phone-lines">USA Office : <b>555-014-2290</b><br>International : <b>1-800-555-0148</b></div>
  </header>
  <nav class="mainnav"><span>HOME</span><span>OUR INCENTIVES</span><span>SAMPLES</span><span>AFFILIATES</span><span>TESTIMONIALS</span><span>FAQ</span><span>CONTACT</span></nav>

  <h1 class="page-title" style="top:130px;font-size:13.5px">Please verify your order and enter your credit card info below</h1>
  <p class="lead" style="left:136px;top:161px;width:400px;font-size:9px;line-height:17px">The information you provide below must match the billing details of where your billing statement is mailed to from your bank</p>

  <div class="card verify-card">
    <svg class="avatar" viewBox="0 0 80 80" role="img" aria-label="Account avatar"><circle cx="40" cy="40" r="40" fill="#7b7b7b"/><circle cx="37" cy="28" r="8" fill="none" stroke="#fff" stroke-width="2.5"/><path d="M20 57c0-10 8-17 17-17 4 0 7 1 10 3" fill="none" stroke="#fff" stroke-width="2.5"/><path d="M20 57h20" stroke="#fff" stroke-width="2.5"/><circle cx="51" cy="51" r="8" fill="none" stroke="#fff" stroke-width="2.5"/><path d="M51 46v10M46 51h10" stroke="#fff" stroke-width="2.5"/></svg>
    <div class="customer">Dana Morrow<br>1200 Elm street<br>Oakridge,CA 90210<br>US<br>5550142290<br>dana@example.com<br>Username : danamorrow</div>
    <div class="fees"><span>One-Time Set Up Fee :</span>$99.00<br><span>Monthly Fee :</span>$99.00/moth<br><span>Total Charged Today :</span>$198.00</div>
    <div class="card-divider"></div>
    <div class="pay-rows">
      <div class="pay-row"><label>Credit Card Type</label><span class="colon">:</span><div class="field">Select One<i class="caret"></i></div></div>
      <div class="pay-row"><label>Credit Card #</label><span class="colon">:</span><div class="field">Select One</div></div>
      <div class="pay-row"><label>Credit Card Exp Month</label><span class="colon">:</span><div class="field">01<i class="caret"></i></div></div>
      <div class="pay-row"><label>Credit Card Exp Year</label><span class="colon">:</span><div class="field">2017<i class="caret"></i></div></div>
      <div class="pay-row"><label>Credit Card CVV2</label><span class="colon">:</span><div class="field"><span></span><i class="caret"></i></div></div>
    </div>
    <p class="cvv-note">The CVV2 is the three digit code on the signature panel of most standard cards, printed after the card number. On some other cards it is the four digit code printed above the credit card number on the front of the card.</p>
    <div class="agree"><i></i>I agree to the Payment Terms and Conditions stated below</div>
    <div class="btn" style="left:158px;top:526px;width:338px;height:29px">SIGNUP NOW</div>
  </div>

  <article class="plan" style="left:63px">
    <div class="plan-head">AL A CARTE PROGRAM</div>
    <div class="plan-prices">1 Certificate Type Each Month<br><b>$49/Mth</b>&nbsp; Month To Month Basis No Contracts<br><b>$239 One</b>&nbsp; Time Payment For 6 Mths Of Service<br><b>$399 One</b>&nbsp; Time Payment For 12 Months Of Service</div>
    <h5>FEATURES:</h5>
    <ul class="features">
      <li><svg width="8" height="7" viewBox="0 0 8 7"><path d="M1 3.5l2 2L7 1" fill="none" stroke="#125fba" stroke-width="1.8"/></svg>Unlimited Certificate Pdf Downloads</li>
      <li><svg width="8" height="7" viewBox="0 0 8 7"><path d="M1 3.5l2 2L7 1" fill="none" stroke="#125fba" stroke-width="1.8"/></svg>Unlimited E-mail Certificates</li>
      <li><svg width="8" height="7" viewBox="0 0 8 7"><path d="M1 3.5l2 2L7 1" fill="none" stroke="#125fba" stroke-width="1.8"/></svg>Unlimited Text/Sms Certificates</li>
      <li><svg width="8" height="7" viewBox="0 0 8 7"><path d="M1 3.5l2 2L7 1" fill="none" stroke="#125fba" stroke-width="1.8"/></svg>Unlimited Api Usage</li>
      <li><svg width="8" height="7" viewBox="0 0 8 7"><path d="M1 3.5l2 2L7 1" fill="none" stroke="#125fba" stroke-width="1.8"/></svg>Unlimited Web Banner Certificates</li>
      <li><svg width="8" height="7" viewBox="0 0 8 7"><path d="M1 3.5l2 2L7 1" fill="none" stroke="#125fba" stroke-width="1.8"/></svg>Full Redemption Tracking</li>
      <li><svg width="8" height="7" viewBox="0 0 8 7"><path d="M1 3.5l2 2L7 1" fill="none" stroke="#125fba" stroke-width="1.8"/></svg>Certificate Distribution Reports</li>
      <li><svg width="8" height="7" viewBox="0 0 8 7"><path d="M1 3.5l2 2L7 1" fill="none" stroke="#125fba" stroke-width="1.8"/></svg>White Label Redemption Site</li>
      <li><svg width="8" height="7" viewBox="0 0 8 7"><path d="M1 3.5l2 2L7 1" fill="none" stroke="#125fba" stroke-width="1.8"/></svg>End User Marketing Videos</li>
      <li><svg width="8" height="7" viewBox="0 0 8 7"><path d="M1 3.5l2 2L7 1" fill="none" stroke="#125fba" stroke-width="1.8"/></svg>Marketing Posters And Flyers</li>
      <li><svg width="8" height="7" viewBox="0 0 8 7"><path d="M1 3.5l2 2L7 1" fill="none" stroke="#125fba" stroke-width="1.8"/></svg>Product Descriptioni Brochures</li>
      <li><svg width="8" height="7" viewBox="0 0 8 7"><path d="M1 3.5l2 2L7 1" fill="none" stroke="#125fba" stroke-width="1.8"/></svg>The Latest Tips</li>
      <li><svg width="8" height="7" viewBox="0 0 8 7"><path d="M1 3.5l2 2L7 1" fill="none" stroke="#125fba" stroke-width="1.8"/></svg>Seperate Redemption Websites</li>
      <li><svg width="8" height="7" viewBox="0 0 8 7"><path d="M1 3.5l2 2L7 1" fill="none" stroke="#125fba" stroke-width="1.8"/></svg>Contact Us 24/7</li>
      <li><svg width="8" height="7" viewBox="0 0 8 7"><path d="M1 3.5l2 2L7 1" fill="none" stroke="#125fba" stroke-width="1.8"/></svg>Affiliate Program</li>
      <li><svg width="8" height="7" viewBox="0 0 8 7"><path d="M1 3.5l2 2L7 1" fill="none" stroke="#125fba" stroke-width="1.8"/></svg>Discount Travel Booking Engine</li>
    </ul>
  </article>

  <article class="plan" style="left:348px">
    <div class="plan-head">UNLIMITED PROGRAM</div>
    <div class="plan-prices">Unlimited Amounts Of All The Certificates<br><b>$99/Mth</b>&nbsp; Month To Month Basis No Contracts<br><b>$495 One</b>&nbsp; Time Payment For 6 Mths Of Service<br><b>$2,295 One</b>&nbsp; Time Payment For 12 Months Of Service</div>
    <h5>FEATURES:</h5>
    <ul class="features">
      <li><svg width="8" height="7" viewBox="0 0 8 7"><path d="M1 3.5l2 2L7 1" fill="none" stroke="#125fba" stroke-width="1.8"/></svg>Unlimited Certificate Pdf Downloads</li>
      <li><svg width="8" height="7" viewBox="0 0 8 7"><path d="M1 3.5l2 2L7 1" fill="none" stroke="#125fba" stroke-width="1.8"/></svg>Unlimited E-mail Certificates</li>
      <li><svg width="8" height="7" viewBox="0 0 8 7"><path d="M1 3.5l2 2L7 1" fill="none" stroke="#125fba" stroke-width="1.8"/></svg>Unlimited Text/Sms Certificates</li>
      <li><svg width="8" height="7" viewBox="0 0 8 7"><path d="M1 3.5l2 2L7 1" fill="none" stroke="#125fba" stroke-width="1.8"/></svg>Unlimited Api Usage</li>
      <li><svg width="8" height="7" viewBox="0 0 8 7"><path d="M1 3.5l2 2L7 1" fill="none" stroke="#125fba" stroke-width="1.8"/></svg>Unlimited Web Banner Certificates</li>
      <li><svg width="8" height="7" viewBox="0 0 8 7"><path d="M1 3.5l2 2L7 1" fill="none" stroke="#125fba" stroke-width="1.8"/></svg>Full Redemption Tracking</li>
      <li><svg width="8" height="7" viewBox="0 0 8 7"><path d="M1 3.5l2 2L7 1" fill="none" stroke="#125fba" stroke-width="1.8"/></svg>Certificate Distribution Reports</li>
      <li><svg width="8" height="7" viewBox="0 0 8 7"><path d="M1 3.5l2 2L7 1" fill="none" stroke="#125fba" stroke-width="1.8"/></svg>White Label Redemption Site</li>
      <li><svg width="8" height="7" viewBox="0 0 8 7"><path d="M1 3.5l2 2L7 1" fill="none" stroke="#125fba" stroke-width="1.8"/></svg>End User Marketing Videos</li>
      <li><svg width="8" height="7" viewBox="0 0 8 7"><path d="M1 3.5l2 2L7 1" fill="none" stroke="#125fba" stroke-width="1.8"/></svg>Marketing Posters And Flyers</li>
      <li><svg width="8" height="7" viewBox="0 0 8 7"><path d="M1 3.5l2 2L7 1" fill="none" stroke="#125fba" stroke-width="1.8"/></svg>Product Descriptioni Brochures</li>
      <li><svg width="8" height="7" viewBox="0 0 8 7"><path d="M1 3.5l2 2L7 1" fill="none" stroke="#125fba" stroke-width="1.8"/></svg>The Latest Tips</li>
      <li><svg width="8" height="7" viewBox="0 0 8 7"><path d="M1 3.5l2 2L7 1" fill="none" stroke="#125fba" stroke-width="1.8"/></svg>Seperate Redemption Websites</li>
      <li><svg width="8" height="7" viewBox="0 0 8 7"><path d="M1 3.5l2 2L7 1" fill="none" stroke="#125fba" stroke-width="1.8"/></svg>Contact Us 24/7</li>
      <li><svg width="8" height="7" viewBox="0 0 8 7"><path d="M1 3.5l2 2L7 1" fill="none" stroke="#125fba" stroke-width="1.8"/></svg>Affiliate Program</li>
      <li><svg width="8" height="7" viewBox="0 0 8 7"><path d="M1 3.5l2 2L7 1" fill="none" stroke="#125fba" stroke-width="1.8"/></svg>Discount Travel Booking Engine</li>
    </ul>
  </article>

  <section class="card terms">
    <h3>Payment Terms &amp; Conditions</h3>
    <svg class="term-icon" style="top:62px" viewBox="0 0 51 51" role="img" aria-label="Recurring billing icon"><circle cx="25.5" cy="25.5" r="25.5" fill="#125fba"/><rect x="17" y="13" width="14" height="22" rx="2" fill="none" stroke="#fff" stroke-width="2"/><path d="M20 19h8M20 23h8M20 27h5" stroke="#fff" stroke-width="1.6"/><rect x="27" y="27" width="9" height="10" rx="1" fill="#125fba" stroke="#fff" stroke-width="1.6"/></svg>
    <div class="term-title" style="top:64px">$99 Recurring Billing</div>
    <div class="term-text" style="top:90px"><p>You must provide a valid billing method. BLRG will immediately charge your account $198. BLRG will continue to debit your account automatically every month for $99. This process will remain in full force until BLRG receives a cancellation notice through the online support ticket system, conveniently located in your password protected control panel area. We must receive the cancellation notice a minimum of 3 business days (not counting holidays or weekends) prior to your next billing date in order to avoid being billed for the following month. Business days are Monday through Friday only, and do not include holidays or weekends</p></div>

    <svg class="term-icon" style="top:206px" viewBox="0 0 51 51" role="img" aria-label="Refund icon"><circle cx="25.5" cy="25.5" r="25.5" fill="#125fba"/><path d="M16 20a11 11 0 1 1-1 9" fill="none" stroke="#fff" stroke-width="2"/><path d="M13 16v6h6" fill="none" stroke="#fff" stroke-width="2"/><text x="25.5" y="31" text-anchor="middle" font-family="Barlow,Arial,sans-serif" font-size="15" font-weight="600" fill="#fff">$</text></svg>
    <div class="term-title" style="top:209px">Refund Policy</div>
    <div class="term-text" style="top:235px"><p>We provide a 3-day refund policy. We will refund you 100%, provided that you request your refund within 3 days of your initial enrollment date. We pay our vendors after 3 days for every member. Therefore, we cannot honor or authorize refund requests after 3 days for reimbursement, as we have already forwarded that money to our clients.</p></div>

    <svg class="term-icon" style="top:310px" viewBox="0 0 51 51" role="img" aria-label="Trial terms document icon"><circle cx="25.5" cy="25.5" r="25.5" fill="#125fba"/><rect x="16" y="13" width="17" height="23" rx="1.5" fill="none" stroke="#fff" stroke-width="2"/><path d="M19 19h11M19 23h11M19 27h8" stroke="#fff" stroke-width="1.6"/><rect x="28" y="29" width="8" height="8" rx="1" fill="#125fba" stroke="#fff" stroke-width="1.6"/></svg>
    <div class="term-title" style="top:312px">30 Day Risk-Free Trial Terms &amp; Conditions</div>
    <div class="term-text" style="top:338px">
      <p>Our incentive marketing program works and we are willing to prove that it works at no risk to our new customers.</p>
      <p>Our incentives work but there is participation required by our customers; you must run incentive marketing campaigns within your business to receive your desired results</p>
      <p>Therefore to participate and to receive the refund you must use our service in the first 30 days from your membership sign up date. To qualify for the 30 day risk free trial refund you need to have at least one (1) paid redemption in the first 30 days of your membership. Redeeming a "Free Healthcare Discount Card" does not satisfy your requirement because it is not a "paid redemption."</p>
      <p>If you are not completely satisfied with the redemption and or the fulfillment process within the first 30 days we will refund 100% of your membership fees per your request.</p>
      <p>By signing up with our company you understand and acknowledge that in order to qualify you must have at least one (1) paid redemption within the first 30 days of your membership.</p>
      <p>You are also required to cancel within 30 days by submitting a 'Support Ticket' from your 'Main Control Panel' account in order to qualify for the refund. Failure in completing these steps will terminate any members' ability to receive the 30-Day Risk Free Trial refund.</p>
    </div>
  </section>

  <footer class="footer" style="top:2089px">
    <h4 style="left:63px">QUICK LINKS</h4>
    <ul class="quick-links"><li>Home</li><li>Our Incentives</li><li>Samples</li><li>Affiliate</li><li>Testimonials</li><li>Faq</li><li>Contact Us</li><li>Terms &amp; Conditions</li><li>Privacy Policy</li><li>Hoteliers</li><li>BLR PDF Flyer</li><li>BLR PDF Brochure</li><li>BLR Certificates List</li><li>How To Use BLR Certificates</li><li>Free Video Ad Mock Up For Marketing</li></ul>
    <div class="foot-divider" style="left:243px"></div>
    <h4 style="left:250px">CONTACT DETAILS</h4>
    <div class="contact-block">
      <svg class="pin" width="7" height="9" viewBox="0 0 7 9"><path d="M3.5 0A3.5 3.5 0 0 0 0 3.5C0 6 3.5 9 3.5 9S7 6 7 3.5A3.5 3.5 0 0 0 3.5 0z" fill="#ccc"/><circle cx="3.5" cy="3.5" r="1.3" fill="#141414"/></svg>
      <div style="padding-left:12px"><b>Brightloom Rewards Group, Inc.</b><br>410 Harbor View Lane<br>Oakridge CA 90210</div>
      <svg class="cal" style="top:53px" width="9" height="8" viewBox="0 0 9 8"><rect x="0" y="1" width="9" height="7" fill="#ccc"/><rect x="1" y="3" width="7" height="4" fill="#141414"/></svg>
      <div style="padding-left:12px;margin-top:22px">Hours: Mon-Fri 8am - 5pm PST<br>Sat-Sun CLOSED</div>
    </div>
    <div class="foot-divider" style="left:477px"></div>
    <div class="foot-brand"><span class="brand-mark"></span><span class="brand-name">BRIGHTLOOM REWARDS</span></div>
    <div class="socials"><i></i><i class="red"></i><i></i><i></i></div>
  </footer>
  <div class="copyright" style="top:2389px">Copyright 2005-2020 Brightloom Rewards Group,Inc. All Rights Reserved<small>C2</small></div>
</section>

</div>
</body>
</html>
```